LumaWireHub full website re-design

I'm looking for a current, cool new design of my website, lumawirehub.com. We sell fiber optic cables and accessories. It hasn't been changed for over 10 years. I would like fresh ideas, not excessive pictures of cables. It has to be easy to navigate because we have over 5k products that we sell. The platform that our site is built on is Prestashop. I've attached many of our popular brands as well as some of our products so you can get an idea of what we sell. I also encourage you to go to our current website to see everything we offer. We are a high end brand and I want to give that impression. The winning designer will likely have ongoing work in the future because we will be making changes and additions to our site. Prestashop experience preferred! Be creative as you want. I would like banner images across the top as well.

Target Market(s)

Men 20-50

Industry/Entity Type

Technology

Coding

Coded - Design and coding required

Number of Pages Required

5+ page

Requirements
Must have
• https://www.vidstreamo.com/watch?v=Q4-RtPw7z2M
Should not have
• cartoons

```html
<!DOCTYPE html>
<html lang="en">
<head>
<meta charset="utf-8">
<title>LumaWireHub</title>
<link href="https://fonts.googleapis.com/css2?family=Roboto:ital,wght@0,400;0,500;0,700;1,400&family=Poppins:wght@400;500;600&display=swap" rel="stylesheet">
<style>
:root{
  --wine:#7c1232;
  --black:#0b0b0b;
  --ink:#111;
  --grey:#777;
  --card:#f1f1f1;
  --footer:#1b1b1b;
  --navy:#0d2c5a;
}
*{margin:0;padding:0;box-sizing:border-box}
html,body{width:1200px;height:3949px;overflow:hidden}
body{font-family:'Roboto',sans-serif;color:var(--ink);background:#fff;position:relative}
a{color:inherit;text-decoration:none}
.abs{position:absolute}
.topbar{left:0;top:0;width:1200px;height:51px;background:var(--black);color:#fff;font-size:14px;font-weight:700}
.topbar a{position:absolute;top:17px}
.header{left:0;top:51px;width:1200px;height:153px;background:#fff}
.call{left:110px;top:38px;display:flex;align-items:center;gap:10px}
.call .dot{width:36px;height:36px;border-radius:50%;background:var(--wine);display:flex;align-items:center;justify-content:center}
.call small{display:block;font-size:13px;font-weight:500;color:#444}
.call b{display:block;font-size:20px;font-weight:500;color:#555}
.brand{left:470px;top:30px;width:260px;text-align:center;display:flex;align-items:center;justify-content:center;gap:10px}
.brand .mark{width:22px;height:22px;border-radius:50%;background:var(--wine)}
.brand span{font-size:34px;font-weight:700;color:var(--wine)}
.search{left:792px;top:36px;width:300px;height:46px;border:1px solid #bbb;border-radius:23px;font-size:12px;color:#666;padding:15px 24px}
.search .go{position:absolute;right:5px;top:5px;width:34px;height:34px;border-radius:50%;background:var(--wine);display:flex;align-items:center;justify-content:center}
.mainnav{top:117px;left:0;width:1200px;text-align:center;font-size:14px;font-weight:500;word-spacing:0}
.mainnav a{margin:0 16px}
.hero{left:0;top:204px;width:1200px;height:685px;background:radial-gradient(circle at 62% 40%,#6fa6e6 0%,#1f56b0 30%,#0d2b6b 70%,#071a44 100%)}
.arrow{width:46px;height:46px;border-radius:50%;background:#0a1530;display:flex;align-items:center;justify-content:center}
.hero-box{left:203px;top:427px;width:794px;height:258px;background:rgba(10,25,60,.72);text-align:center;color:#fff}
.hero-box h1{font-size:33px;font-weight:700;line-height:43px;margin-top:46px}
.btn{display:inline-block;background:var(--wine);color:#fff;font-size:14px;font-weight:700;padding:15px 20px}
.tile{top:901px;width:383px;height:266px}
.tile .label{position:absolute;left:36px;top:103px;width:310px;height:61px;background:#fff;font-size:20px;font-weight:500;display:flex;align-items:center;justify-content:center}
.kicker{top:1269px;width:1200px;text-align:center;color:var(--wine);font-size:14px;font-weight:500}
.h2{width:1200px;text-align:center;font-size:38px;font-weight:700}
.prod{top:1374px;width:230px}
.prod .img{height:258px;background:linear-gradient(150deg,#f7f7f7,#e4e4e4);border-radius:4px;position:relative}
.prod .tag{position:absolute;left:16px;top:18px;background:var(--wine);color:#fff;font-size:12px;padding:5px 12px;border-radius:12px}
.prod .price{margin-top:18px;font-size:20px;font-weight:700;color:#444;text-decoration:line-through}
.prod .name{margin-top:6px;font-size:20px;line-height:26px;color:#333}
.shopall{top:1808px;width:1200px;text-align:center;font-size:21px;font-weight:700;color:var(--wine);text-decoration:underline}
.testi{left:0;top:1937px;width:1200px;height:401px;background:linear-gradient(110deg,#0e4d72,#0f5f82 45%,#0a3458);color:#fff;text-align:center}
.testi h2{font-size:38px;font-weight:700;margin-top:86px}
.testi p{font-style:italic;font-size:13px;line-height:21px;width:780px;margin:22px auto 0}
.testi h4{font-size:20px;font-weight:500;margin-top:26px}
.testi small{display:block;font-size:13px;margin-top:6px}
.feat{top:2440px;width:230px}
.feat h3{font-size:21px;font-weight:500}
.feat p{font-size:13px;line-height:21px;color:var(--grey);margin-top:12px}
.promo{top:2640px;width:480px;height:253px;color:#fff}
.promo .txt{position:absolute;left:185px;top:36px}
.promo small{font-size:14px;font-weight:500}
.promo h3{font-size:26px;font-weight:500;line-height:34px;margin-top:6px}
.promo a{position:absolute;top:158px;font-size:15px;font-weight:700;text-decoration:underline;white-space:nowrap}
.blog{top:3055px;width:316px;height:359px}
.blog .card{position:absolute;left:20px;top:225px;width:276px;height:116px;background:#fff;text-align:center}
.blog .date{font-size:13px;font-weight:700;color:var(--wine);letter-spacing:3px;margin-top:22px}
.blog h4{font-size:20px;font-weight:700;line-height:26px;margin-top:10px}
.footer{left:0;top:3517px;width:1200px;height:432px;background:var(--footer);color:#fff;font-family:'Poppins',sans-serif}
.fcol{top:108px}
.fcol h5{font-size:15px;font-weight:600;margin-bottom:12px}
.fcol li{list-style:none;font-size:13px;line-height:28px}
.news p{font-size:13px;line-height:28px;width:290px}
.field{margin-top:12px;width:284px;height:48px;background:#fff;border-radius:24px;color:#666;font-size:12px;padding:16px 16px;position:relative}
.field .send{position:absolute;right:3px;top:3px;width:50px;height:42px;border-radius:21px;background:var(--wine);display:flex;align-items:center;justify-content:center}
.soc{display:inline-block;width:28px;height:28px;border:1px solid #fff;border-radius:50%;margin-right:8px}
.copy{top:371px;width:1200px;text-align:center;font-size:13px}
</style>
</head>
<body>

<div class="abs topbar">
  <a style="left:110px">LINE CARD</a>
  <a style="left:218px">GOV/EDU BUYERS</a>
  <a style="left:376px">RESELLERS</a>
  <a style="left:941px">LOGIN</a>
  <a style="left:1017px">REGISTER</a>
</div>

<header class="abs header">
  <div class="abs call">
    <span class="dot"><svg width="16" height="16" viewBox="0 0 24 24"><path fill="#fff" d="M6.6 10.8a15 15 0 006.6 6.6l2.2-2.2c.3-.3.7-.4 1-.2 1.1.4 2.3.6 3.6.6.6 0 1 .4 1 1V20c0 .6-.4 1-1 1A17 17 0 013 4c0-.6.4-1 1-1h3.5c.6 0 1 .4 1 1 0 1.3.2 2.5.6 3.6.1.3 0 .7-.2 1z"/></svg></span>
    <div><small>Call us Today :</small><b>+1 888 888 8888</b></div>
  </div>
  <div class="abs brand"><span class="mark"></span><span>LumaWireHub</span></div>
  <div class="abs search">Enter your keyword
    <span class="go"><svg width="13" height="13" viewBox="0 0 24 24"><circle cx="10" cy="10" r="6" stroke="#fff" stroke-width="3" fill="none"/><path d="M15 15l5 5" stroke="#fff" stroke-width="3"/></svg></span>
  </div>
  <nav class="abs mainnav"><a>30 MIN QUOTE</a><a>CUSTOM CABLE</a><a>PURCHASING</a></nav>
</header>

<section class="abs hero" role="img" aria-label="Photo of a fiber optic cable with glowing coloured strands">
  <div class="abs arrow" style="left:32px;top:319px"><svg width="12" height="12" viewBox="0 0 12 12"><path d="M8 1L3 6l5 5" stroke="#fff" stroke-width="1.6" fill="none"/></svg></div>
  <div class="abs arrow" style="left:1122px;top:319px"><svg width="12" height="12" viewBox="0 0 12 12"><path d="M4 1l5 5-5 5" stroke="#fff" stroke-width="1.6" fill="none"/></svg></div>
  <div class="abs hero-box">
    <h1>GOVERMENT, MILITARY AND EDUCATIONAL<br>PREFERRED PRICING AVAILABLE</h1>
    <a class="btn" style="margin-top:18px">SHOP NOW</a>
  </div>
</section>

<div class="abs tile" style="left:10px;background:linear-gradient(135deg,#7fb4d6,#d9685e 45%,#3d7fa8)" role="img" aria-label="Fiber cable over a circuit board"><div class="label">EXPRESS CUSTOM CABLES</div></div>
<div class="abs tile" style="left:409px;background:linear-gradient(160deg,#1a6a96,#0a2a4a 60%,#05121f)" role="img" aria-label="Glowing fiber cable ends"><div class="label">LIFETIME WARRANTY</div></div>
<div class="abs tile" style="left:808px;background:linear-gradient(150deg,#2a3f8f,#4f72c8 50%,#10205a)" role="img" aria-label="Fiber light strands in blue"><div class="label">FREE GROUND SHIPPING</div></div>

<div class="abs kicker">WHOLE COLLECTION AVAILABLE</div>
<h2 class="abs h2" style="top:1298px">FEATURED PRODUCTS</h2>

<div class="abs prod" style="left:110px"><div class="img" role="img" aria-label="LC duplex connector"><span class="tag">-20%</span></div><div class="price">$8.99</div><div class="name">OM1 LC LC Fiber Patch Cable | 1Gb Duplex 62.5/125 Multimode</div></div>
<div class="abs prod" style="left:358px"><div class="img" role="img" aria-label="LC duplex connector"></div><div class="price">$9.59</div><div class="name">OM2 LC LC Duplex Fiber Patch Cable 50/125 Multimode</div></div>
<div class="abs prod" style="left:608px"><div class="img" role="img" aria-label="Aqua duplex patch cable"><span class="tag">-20%</span></div><div class="price">$9.95</div><div class="name">OM3 LC LC Duplex Fiber Patch Cable 10Gb Multimode 50/125</div></div>
<div class="abs prod" style="left:858px"><div class="img" role="img" aria-label="LC duplex connector"></div><div class="price">$8.99</div><div class="name">OM4 LC LC Fiber Patch Cable | 100G Duplex 50/125 Multimode</div></div>

<a class="abs shopall">Shop All Products »</a>

<section class="abs testi" role="img" aria-label="Cross-section of a multi-strand cable in teal light">
  <div class="abs arrow" style="left:32px;top:177px"><svg width="12" height="12" viewBox="0 0 12 12"><path d="M8 1L3 6l5 5" stroke="#fff" stroke-width="1.6" fill="none"/></svg></div>
  <div class="abs arrow" style="left:1122px;top:177px"><svg width="12" height="12" viewBox="0 0 12 12"><path d="M4 1l5 5-5 5" stroke="#fff" stroke-width="1.6" fill="none"/></svg></div>
  <h2>OUR CLIENT SAYS</h2>
  <p>"Lorem ipsum dolor sit amet, consectetur adipiscing elit, sed do eiusmod tempor incididunt ut labore et dolore magna aliqua. Ut enim ad minim veniam, quis nostrud exercitation ullamco laboris nisi ut aliquip ex ea commodo consequat. Duis aute irure dolor in reprehenderit in voluptate velit esse cillum dolore eu fugiat nulla pariatur. Excepteur sint occaecat cupidatat non proident, sunt in culpa qui officia deserunt mollit anim id est laborum."</p>
  <h4>JOHN DOE</h4>
  <small>Company name</small>
</section>

<div class="abs feat" style="left:110px"><h3>FREE SHIPPING</h3><p>Lorem ipsum dolor sit amet, cons ectetur adipiscing elit, sed do eiusmod tempor</p></div>
<div class="abs feat" style="left:496px"><h3>ONLINE SUPPORT</h3><p>Lorem ipsum dolor sit amet, cons ectetur adipiscing elit, sed do eiusmod tempor</p></div>
<div class="abs feat" style="left:881px"><h3>GIFT VOUCHER</h3><p>Lorem ipsum dolor sit amet, cons ectetur adipiscing elit, sed do eiusmod tempor</p></div>

<div class="abs promo" style="left:110px;background:linear-gradient(120deg,#2f3b3d,#17262a 60%,#0f1c20)" role="img" aria-label="Armoured copper cables">
  <div class="txt"><small>FLAT 30% OFF</small><h3>BUY COLLECTION<br>DESIGN</h3><a>SHOP NOW</a></div>
</div>
<div class="abs promo" style="left:608px;background:linear-gradient(120deg,#1c2f7a,#12237a 50%,#0b1760)" role="img" aria-label="Multicoloured cable wires">
  <div class="txt"><small>FLAT 30% OFF</small><h3>BUY COLLECTION<br>DESIGN</h3><a>SHOP NOW</a></div>
</div>

<h2 class="abs h2" style="top:2988px">FROM THE BLOG</h2>
<div class="abs blog" style="left:110px;background:linear-gradient(135deg,#9aa4ab,#5d6a73 60%,#3a434a)" role="img" aria-label="Technician working on an electrical panel"><div class="card"><div class="date">JAN 20,2021</div><h4>Lorem ipsum dolor sit am et, consectetur</h4></div></div>
<div class="abs blog" style="left:441px;background:linear-gradient(135deg,#c65a2e,#8a6e6a 50%,#3f5b82)" role="img" aria-label="Copper cable cross-sections"><div class="card"><div class="date">JAN 20,2021</div><h4>Lorem ipsum dolor sit am et, consectetur</h4></div></div>
<div class="abs blog" style="left:772px;background:linear-gradient(135deg,#c9ccd6,#4b55b5 50%,#2a2f6e)" role="img" aria-label="Network switch with blue patch cables"><div class="card"><div class="date">JAN 20,2021</div><h4>Lorem ipsum dolor sit am et, consectetur</h4></div></div>

<footer class="abs footer">
  <div class="abs fcol" style="left:113px"><h5>NAVIGATION</h5><ul><li>Home</li><li>About</li><li><a href="https://www.vidstreamo.com/watch?v=Q4-RtPw7z2M">Our videos</a></li><li>Contact</li><li>Privacy</li><li>Terms</li></ul></div>
  <div class="abs fcol" style="left:319px"><h5>OUR SERVICES</h5><ul><li>Solution</li><li>Pricing</li><li>Resources</li><li>About us</li><li>Support Wiki</li></ul></div>
  <div class="abs fcol" style="left:547px"><h5>CONTACT US</h5><ul><li>&#9742;&nbsp; +1 888 888 8888</li><li>&#9679;&nbsp; North America Halden</li><li style="padding-left:20px">Security USA</li></ul>
    <h5 style="margin-top:10px">FOLLOW US</h5><span class="soc"></span><span class="soc"></span></div>
  <div class="abs fcol news" style="left:810px;top:104px"><h5>RECEIVE OUR NEWSLETTER</h5><p>Sign up today to get resources on how to attract and retain more customers!</p>
    <div class="field">Email Address<span class="send"><svg width="18" height="18" viewBox="0 0 24 24"><path fill="#fff" d="M2 12l20-9-6 19-4-8z"/></svg></span></div></div>
  <div class="abs copy">Copyright © 2021. All Rights Reserved</div>
</footer>

</body>
</html>
```